依頼詳細
【仕様】
『資格完全攻略 突破 ケアワーカー ノート&ドリル 2014 基礎分野編』『資格完全攻略 突破 ケアワーカー ノート&ドリル 2014 応用分野編』は同じ仕様となります。
・B5(182 × 257 ㎜)
・背幅はおよそ20㎜です(修正有)。
・本文は横書ですので左綴じとなります。
・カバー(表1、表4、背表紙):4C(フルカラー)
・表紙(表1、表4、背表紙):1C
・扉:1C

※表紙・扉のデザインはカバーデザインに基づいたもので、「書名」「編者名」「社名」だけが入っているもので結構です。
記載項目
【デザインについて】
・同資格のための参考書・問題集・ワークブックは類書が数多くあり、なかなか差別化が図れないのが現状です。今回は、「資格受験用テキスト・問題集」によく見られるようなキャッチコピーが踊るデザインではなく、すっきりとした知的かつスマートなデザインを希望します。
・書籍の内容は堅いですが、読者が手に取りやすい親しみやすさも加味してください。
・『要点整理と演習集』のデザインにはとらわれませんし、イラスト等を加えていただいても結構です。
・タイトルの文字についてですが、「ケアワーカー」「突破」「2014」「基礎分野編」「専門科目編」が目に付くようにしてください。特に「ケアワーカー」の文言については100級以上の大きさでお願いをします。
・2つの書籍でデザインに盛り込む内容(文字)が異なります。書名、編者名等のデザインに盛り込む内容(文字)は添付ファイルを参照してください。

その他、ご不明な点は、お気軽にお問い合わせください。
希望イメージ
シンプル 複雑
単色 カラフル
暗い 明るい
日常 高級
遊び心 厳粛
未来的 伝統的
女性的 男性的
希望する色
特になし
納品ファイル
• イラストレーター形式 (.ai)
補足説明
■ 選んだ理由

①従来の弊社の書籍とは違うやわらかいイメージ。
②他社の類書との差別化がはかれるデザイン。
③書籍の内容(テキスト・問題集)がもつ「堅い」イメージをやわらげてくれるデザイン。

■ 提案者全員のお礼・コメント

この度は多くのご提案ありがとうございました。
ご応募くださった皆様の提案はとてもバラエティに富み、素晴らしいものが多く迷いましたが、上記の理由により選定させていただきました。
それぞれの提案に社内では「他の書籍ならこのデザインがいい」といった声もきかれました。今回の書籍では惜しくも採用にいたらなかった提案も違う案件によっては十分に採用される可能性がありました。
今後もこのようなデザインをしていただきたい案件がございます。またの機会にも是非ご応募くださいますようお願いいたします。

```html
<!DOCTYPE html>
<html lang="ja">
<head>
<meta charset="utf-8">
<title>資格完全攻略 突破 ケアワーカー ノート&ドリル 2014 基礎分野編</title>
<link rel="stylesheet" href="https://fonts.googleapis.com/css2?family=Noto+Sans+JP:wght@500;700;900&display=swap">
<style>
  :root {
    --paper: #ececec;
    --paper-edge: #b9b9b9;
    --ink: #2b2b2b;
    --ink-soft: #3c3c3c;
    --band: #333333;
    --seal: #3a3a3a;
    --white: #ffffff;
    --pencil-light: #d6d6d6;
    --pencil-dark: #8d8d8d;
  }
  * { margin: 0; padding: 0; box-sizing: border-box; }
  html, body { width: 848px; height: 1200px; overflow: hidden; }
  body { font-family: "Noto Sans JP", sans-serif; color: var(--ink); }
  .cover {
    position: relative; width: 848px; height: 1200px; overflow: hidden;
    background: radial-gradient(ellipse at 45% 40%, var(--paper) 0%, #dedede 55%, var(--paper-edge) 100%);
  }
  .series {
    position: absolute; left: 106px; top: 84px;
    font-size: 46px; font-weight: 700; letter-spacing: 2px; line-height: 1.2; color: var(--ink);
  }
  .stamp {
    position: absolute; left: 500px; top: 62px; width: 160px; height: 80px;
    border: 5px solid var(--ink); border-radius: 10px; transform: rotate(-6deg);
    display: flex; align-items: center; justify-content: center;
    font-size: 54px; font-weight: 900; color: var(--ink); letter-spacing: 2px; line-height: 1;
  }
  .title {
    position: absolute; left: 100px; top: 152px;
    font-size: 88px; font-weight: 900; letter-spacing: 0; line-height: 1; color: var(--ink);
  }
  .ribbon { position: absolute; left: 100px; top: 262px; width: 460px; height: 74px; }
  .ribbon svg { position: absolute; inset: 0; }
  .ribbon-text {
    position: absolute; inset: 0; display: flex; align-items: center; justify-content: center;
    font-size: 46px; font-weight: 700; color: var(--white); letter-spacing: 1px; line-height: 1;
  }
  .year {
    position: absolute; left: 330px; top: 350px;
    font-size: 80px; font-weight: 900; letter-spacing: 2px; line-height: 1.2; color: var(--ink);
  }
  .seal {
    position: absolute; left: 540px; top: 312px; width: 178px; height: 178px;
    border-radius: 50%; background: var(--seal);
    display: flex; flex-direction: column; align-items: center; justify-content: center;
    color: var(--white); font-size: 48px; font-weight: 900; line-height: 1.1;
  }
  .credits {
    position: absolute; left: 0; width: 848px; top: 490px; text-align: center;
    font-size: 28px; font-weight: 700; line-height: 1.5; color: var(--ink-soft);
  }
  .pencil-art {
    position: absolute; left: 420px; top: 620px; width: 428px; height: 300px;
    background: linear-gradient(215deg, var(--pencil-light) 0%, #c2c2c2 40%, var(--pencil-dark) 75%, rgba(141,141,141,0) 100%);
    opacity: .5;
  }
  .publisher {
    position: absolute; left: 0; width: 848px; top: 1040px; text-align: center;
    font-size: 30px; font-weight: 700; line-height: 1.2; color: var(--ink-soft);
  }
</style>
</head>
<body>
  <main class="cover">
    <div class="series">資格完全攻略</div>
    <div class="stamp">突破</div>
    <h1 class="title">ケアワーカー</h1>
    <div class="ribbon">
      <svg width="460" height="74" viewBox="0 0 460 74">
        <polygon points="0,0 460,0 444,37 460,74 0,74 16,37" fill="var(--band)"/>
      </svg>
      <div class="ribbon-text">ノート&amp;ドリル</div>
    </div>
    <div class="year">2014</div>
    <div class="seal"><span>基礎</span><span>分野</span></div>
    <div class="credits">
      <p class="supervisor">高峰 透 監修</p>
      <p class="editor">ケアワーカー資格研究会 編集</p>
    </div>
    <div class="pencil-art" role="img" aria-label="斜めに置かれた鉛筆のイラスト"></div>
    <div class="publisher">㈱あおば</div>
  </main>
</body>
</html>
```